Church Bulletin Ad (see attached sample)

Create a New Church Bulletin Ad. I have attached some samples of what we would like to have in the ad. (1) Marrowfield Realty Thorne Logo (2) Headshot (3) Lena Vasko & Greta Vasko, Real Estate Team (4) Phone number (5) Email address (6) St Aldwin Parishioners for over 40 Years. We would like for the ad to be clean and modern. NO OTHER IMAGES besides headshots and Marrowfield Realty Thorne Logo.

Target Market(s)

Church community

Industry/Entity Type

Real Estate

Font styles to use
Sans Serif
Other font styles liked:
• Modern Font

Colors
0054AA
0677BA
7BADD7
CADEEF
E8F1F8

Requirements
Must have
• Marrowfield Realty Thorne Logo; Headshot; Ad size is 4.5"x1.62"

```html
<!DOCTYPE html>
<html lang="en">
<head>
<meta charset="utf-8">
<title>Vasko Real Estate Team – Bulletin Ad</title>
<link rel="stylesheet" href="https://fonts.googleapis.com/css2?family=Montserrat:wght@600;700;800&family=Oswald:wght@600;700&display=swap">
<style>
  :root {
    --page-bg: #e6e8eb;
    --navy: #1b3566;
    --navy-deep: #172e5a;
    --brand-blue: #1479b8;
    --bright-blue: #0f83c4;
    --pale-blue: #cadeef;
    --white: #ffffff;
    --photo-light: #e9eef2;
    --photo-mid: #b9c3cc;
    --photo-dark: #3b3b3f;
  }
  * { box-sizing: border-box; margin: 0; padding: 0; }
  html, body {
    width: 1200px; height: 750px; overflow: hidden;
    background: var(--page-bg);
  }
  .ad {
    position: absolute; left: 40px; top: 173px;
    width: 1120px; height: 403px;
    overflow: hidden;
    font-family: "Montserrat", sans-serif;
    color: var(--white);
  }
  .ad-shapes { position: absolute; inset: 0; }
  .headline {
    position: absolute; left: 664px; top: 30px; width: 417px;
    font-family: "Oswald", sans-serif; font-weight: 700;
    font-size: 55px; line-height: 1; letter-spacing: -0.5px;
    text-align: center; white-space: nowrap;
  }
  .headline-box {
    position: absolute; left: 665px; top: 94px; width: 416px; height: 49px;
    background: var(--white); border-radius: 4px;
    color: var(--navy);
    font-weight: 800; font-size: 38px; letter-spacing: 7px;
    display: flex; align-items: center; justify-content: center;
    padding-left: 7px;
  }
  .team {
    position: absolute; left: 666px; top: 162px;
    border-left: 2px solid var(--brand-blue);
    padding-left: 11px;
    font-weight: 700; font-size: 22px; line-height: 30px;
    white-space: nowrap;
  }
  .brand-box {
    position: absolute; left: 591px; top: 237px; width: 111px; height: 98px;
    border: 4px solid var(--white); background: var(--navy);
    display: flex; align-items: center; justify-content: center;
    text-align: center;
    font-weight: 700; font-size: 13px; line-height: 17px;
  }
  .phone {
    position: absolute; left: 735px; top: 250px; width: 346px; height: 43px;
    border: 2px solid var(--white); border-radius: 22px;
    display: flex; align-items: center;
    padding-left: 4px;
    font-weight: 700; font-size: 31px; letter-spacing: 0.5px;
  }
  .phone-icon { width: 36px; height: 36px; margin-right: 14px; flex: none; }
  .email {
    position: absolute; left: 737px; top: 298px;
    font-weight: 600; font-size: 21px; white-space: nowrap;
  }
  .parish {
    position: absolute; right: 39px; top: 350px;
    font-family: "Oswald", sans-serif; font-weight: 600;
    font-size: 27px; white-space: nowrap;
  }
</style>
</head>
<body>
  <section class="ad">
    <svg class="ad-shapes" viewBox="0 0 1120 403" width="1120" height="403">
      <defs>
        <linearGradient id="headshotTone" x1="0" y1="0" x2="1" y2="1">
          <stop offset="0" stop-color="var(--photo-light)"/>
          <stop offset="0.55" stop-color="var(--photo-mid)"/>
          <stop offset="1" stop-color="var(--photo-dark)"/>
        </linearGradient>
      </defs>
      <rect class="bg-navy" width="1120" height="403" fill="var(--navy)"/>
      <polygon class="bottom-sweep" points="560,403 700,335 1120,335 1120,403" fill="var(--navy-deep)"/>
      <polygon class="accent-light" points="560,0 720,0 800,201 720,403 560,403" fill="var(--brand-blue)"/>
      <polygon class="accent-dark" points="590,0 670,0 748,201 670,403 590,403" fill="#1a5d99"/>
      <rect class="contact-band" x="591" y="235" width="529" height="100" fill="var(--bright-blue)"/>
      <polygon class="bottom-band" points="620,403 680,335 1120,335 1120,403" fill="var(--navy)"/>
      <polygon class="bottom-accent" points="620,403 680,335 1000,335 940,403" fill="#1f5a97" opacity="0.55"/>
      <polygon class="headshot-area" role="img" aria-label="Headshot of Lena Vasko Hale and Greta Vasko"
               points="0,0 538,0 615,201 538,403 0,403" fill="url(#headshotTone)"/>
    </svg>

    <h1 class="headline">ENERGY EXCELLENCE</h1>
    <div class="headline-box">EXPERIENCE</div>

    <p class="team">Lena Vasko Hale &amp; Greta Vasko<br>Real Estate Team</p>

    <div class="brand-box">Marrowfield<br>Realty<br>Thorne</div>

    <div class="phone">
      <svg class="phone-icon" viewBox="0 0 36 36" aria-hidden="true">
        <circle cx="18" cy="18" r="16" fill="none" stroke="var(--white)" stroke-width="2.5"/>
        <path d="M12.5 10.5c1-.9 2.2-.8 2.8.3l1.4 2.6c.5.9.2 1.8-.6 2.4l-.9.7c.8 1.9 2.3 3.4 4.2 4.2l.7-.9c.6-.8 1.5-1.1 2.4-.6l2.6 1.4c1.1.6 1.2 1.8.3 2.8l-1.1 1.2c-1.3 1.3-3.5 1.4-6.2-.3-2.3-1.4-4.3-3.4-5.7-5.7-1.7-2.7-1.6-4.9-.3-6.2z" fill="var(--white)"/>
      </svg>
      (206) 555-0148
    </div>
    <p class="email">vaskohaleteam@mrthorne.com</p>

    <p class="parish">St Aldwin Parishioners For Over 40 Years.</p>
  </section>
</body>
</html>
```